Harborline Open Cinema Gathering 20th Annual Poster

September 2017 will to the 20th Annual Harborline Open Cinema Gathering. We have a new logo and need a new modern stylish poster designed. One that shows creativity, imagination, style and class. Think outside the box. Modern and new.

Dates are: September 7th - 13th 2017

Our tagline:
"Something for Everyone from Around the World"

Target Market(s)

film festival goings - 35 - 70 age range - 58% female 42% males - movie lovers - movie goers

Industry/Entity Type

Movie

Font styles to use
Script

Requirements
Must have
• modern style celebrating 20 years - cool design - chic and stylish - upscale - high society - think Abstract
Nice to have
• thinking outside the box - not just simple film reel - think Abstract! Not just your standard film items. Creative in your idea and design
Should not have
• no CLIP ART

```html
<!DOCTYPE html>
<html lang="en">
<head>
<meta charset="utf-8">
<title>Harborline Open Cinema Gathering – 20th Annual</title>
<link rel="stylesheet" href="https://fonts.googleapis.com/css2?family=Poiret+One&family=Allura&display=swap">
<style>
  :root {
    --paper: #ffffff;
    --ink: #111111;
    --festival-red: #b3243a;
    --curtain-dark: #a3121a;
    --curtain-mid: #d11a22;
    --seat-dark: #8a1622;
    --seat-mid: #b51f2e;
    --navy: #101b3e;
    --rule: #222222;
  }
  * { margin: 0; padding: 0; box-sizing: border-box; }
  html, body { width: 810px; height: 1200px; overflow: hidden; background: var(--paper); }
  .poster {
    position: relative;
    width: 810px;
    height: 1200px;
    background: var(--paper);
    font-family: "Poiret One", sans-serif;
    color: var(--ink);
    overflow: hidden;
  }
  .curtain-area {
    position: absolute;
    top: 0;
    width: 120px;
    height: 840px;
  }
  .curtain-area--left {
    left: 0;
    background: linear-gradient(90deg, var(--curtain-dark), var(--curtain-mid));
  }
  .curtain-area--right {
    right: 0;
    background: linear-gradient(90deg, var(--curtain-mid), var(--curtain-dark));
  }
  .seating-area {
    position: absolute;
    left: 0; top: 908px;
    width: 810px; height: 292px;
    background: linear-gradient(180deg, var(--seat-mid) 0%, var(--seat-dark) 100%);
  }
  .brand-mark {
    position: absolute;
    left: 342px; top: 27px;
    width: 126px; height: 126px;
    border-radius: 50%;
    background: var(--navy);
    display: flex; align-items: center; justify-content: center;
  }
  .brand-name {
    font-family: "Poiret One", sans-serif;
    font-size: 30px;
    letter-spacing: 3px;
    color: var(--paper);
  }
  .centered { position: absolute; left: 0; width: 810px; text-align: center; }
  .edition { top: 170px; font-size: 36px; line-height: 44px; }
  .rule { position: absolute; left: 274px; width: 262px; height: 1px; background: var(--rule); }
  .rule--top { top: 232px; }
  .rule--mid { top: 495px; }
  .rule--bottom { top: 573px; }
  .title-line { font-size: 60px; line-height: 1; letter-spacing: 1px; font-weight: 400; }
  .title-line--one { top: 262px; }
  .title-line--two { top: 336px; color: var(--festival-red); }
  .title-line--three { top: 410px; -webkit-text-stroke: 1.2px var(--ink); }
  .dates { top: 512px; font-size: 36px; line-height: 44px; }
  .tagline {
    font-family: "Allura", cursive;
    font-size: 64px;
    line-height: 1;
  }
  .tagline--one { top: 612px; }
  .tagline--two { top: 698px; }
</style>
</head>
<body>
<main class="poster">
  <div class="curtain-area curtain-area--left" role="img" aria-label="Red stage curtain tied back on the left"></div>
  <div class="curtain-area curtain-area--right" role="img" aria-label="Red stage curtain tied back on the right"></div>
  <div class="seating-area" role="img" aria-label="Rows of red velvet cinema seats"></div>

  <div class="brand-mark"><span class="brand-name">HOCG</span></div>

  <p class="centered edition">20th Annual</p>
  <div class="rule rule--top"></div>
  <h1>
    <span class="centered title-line title-line--one">HARBORLINE</span>
    <span class="centered title-line title-line--two">OPEN CINEMA</span>
    <span class="centered title-line title-line--three">GATHERING</span>
  </h1>
  <div class="rule rule--mid"></div>
  <p class="centered dates">September 7th - 13th 2017</p>
  <div class="rule rule--bottom"></div>
  <p class="centered tagline tagline--one">Something for Everyone</p>
  <p class="centered tagline tagline--two">from Around the World</p>
</main>
</body>
</html>
```